Website Makeover for Local small business Law Enforcement Vendor

We are a very small business (2-3 employees) that provides training and study products to police officers study for promotion exams, as well as other law enforcement training. We currently use NetHarbor as our hosting company and we use one of there template makers for our web design. So your design will have to be compatible and easy for a novice to upload in place of the current NetHarbor template. This is vital. You will need to provide detailed instructions on how to convert your design to our existing website.

The website has an accompanying web store were customers can buy products, ultimately we'd like a full integration between the main website and the on-line store. However, we can't afford to have our site or store down for any period of time.

Our web address is www.brixlaneprep.us It is simple and unprofessional. We'd like it to be modern and inviting.

We have four main categories of services/products:

1. Police Promotion Exam Preparation
2. Police Training
3. Police Entrance Exam Services
4. Police Department Services

We are open to your expertise and suggestions. We don't have many photos/graphics to offer you.
Updates

Target Market(s)

Police officers and Police Departments

Industry/Entity Type

Small Business

Requirements
Must have
• Easy conversion to existing NetHarbor hosting - with detailed instructions.

Link to our webstore - unless you can better integrate to existing site.

The ability for a novice to modify content and load updates with ease.
Nice to have
• The ability to post PDF's and/or Word documents for download by others (registration forms etc.)

```html
<!DOCTYPE html>
<html lang="en">
<head>
<meta charset="utf-8">
<title>Brixlane Consulting – Police Promotion &amp; Training</title>
<link href="https://fonts.googleapis.com/css2?family=Open+Sans:wght@400;600;700;800&family=Oswald:wght@500;700&display=swap" rel="stylesheet">
<style>
:root{
  --navy:#0f2a6b;
  --navy-dark:#0a1f52;
  --blue:#1f56b8;
  --gold:#f3b51c;
  --orange:#f29b1d;
  --red:#d7262e;
  --page:#f2f2f2;
  --rule:#dcdcdc;
  --ink:#333;
  --muted:#7a7a7a;
  --white:#fff;
}
*{box-sizing:border-box;margin:0;padding:0}
html,body{width:699px;height:1200px;overflow:hidden}
body{background:var(--page);font-family:"Open Sans",Arial,sans-serif;color:var(--ink);position:relative}
.header{height:66px;background:var(--white);position:relative}
.brand{position:absolute;left:100px;top:8px;display:flex;align-items:center;gap:6px;z-index:3}
.brand .mark{width:58px;height:58px;border-radius:50%;background:var(--gold);border:4px solid var(--navy)}
.brand .name{font-weight:800;font-size:11px;color:var(--navy);line-height:1.1;width:70px;text-transform:uppercase}
.cta-courses{position:absolute;left:378px;top:22px;background:var(--blue);color:var(--white);font-size:9px;font-weight:600;padding:5px 9px;border-radius:2px}
.phone{position:absolute;left:512px;top:20px;display:flex;align-items:center;gap:6px;color:var(--blue);font-weight:700;font-size:15px}
.nav{height:16px;background:#e9e9e9;border-top:1px solid var(--rule);border-bottom:1px solid var(--rule)}
.nav ul{list-style:none;display:flex;gap:14px;margin-left:180px;font-size:7px;color:#555;line-height:14px}
.wrap{width:500px;margin:0 auto}
.hero{margin-top:6px;height:262px;position:relative;overflow:hidden;
  background:linear-gradient(120deg,#a9c4e6 0%,#e8eef6 30%,#b83a3a 48%,#f1f1f1 56%,#2b3f6e 70%,#15254c 100%)}
.hero .tag{position:absolute;right:50px;top:30px;font-family:Oswald,sans-serif;color:var(--white);font-size:15px;letter-spacing:.5px}
.hero h1{position:absolute;left:22px;top:150px;font-family:Oswald,sans-serif;color:var(--white);font-size:24px;line-height:1.1;font-weight:700;text-shadow:0 1px 3px rgba(0,0,0,.5)}
.hero .btns{position:absolute;left:22px;top:222px;display:flex;gap:6px}
.btn-red{background:var(--red);color:var(--white);font-size:9px;font-weight:700;padding:5px 10px;border-radius:2px}
.btn-gold{background:var(--gold);width:22px;border-radius:2px}
.hero .arrow{position:absolute;top:118px;width:16px;height:16px;border-radius:50%;background:rgba(255,255,255,.6)}
.services{display:flex;justify-content:space-between;margin-top:18px;padding:0 6px}
.svc{width:112px;text-align:center}
.svc .pic{width:70px;height:70px;border-radius:50%;margin:0 auto;border:3px solid var(--white);box-shadow:0 0 0 1px var(--rule);background:linear-gradient(160deg,#6d86b0,#23355f)}
.svc h3{font-size:7.5px;font-weight:700;color:var(--navy);margin-top:10px;line-height:1.25;height:20px}
.svc p{font-size:6px;color:var(--muted);line-height:1.4;margin-top:4px;height:42px}
.btn-navy{display:inline-block;background:var(--navy);color:var(--white);font-size:7px;font-weight:600;padding:4px 12px;border-radius:2px;margin-top:6px}
.rule{height:1px;background:var(--rule);margin:16px 0 10px}
.rule.lower{margin-top:30px}
.cols{display:flex;justify-content:space-between}
.col{width:240px}
.col h2{font-size:10px;font-weight:700;color:var(--navy);text-transform:uppercase;padding-bottom:5px;border-bottom:1px solid var(--rule)}
.col h2 span{color:var(--orange)}
.products{list-style:none;margin-top:10px}
.products li{display:flex;align-items:center;gap:10px;font-size:7px;font-weight:700;color:var(--navy);height:22px}
.products i{width:12px;height:14px;background:var(--navy);border-radius:2px;display:block}
.form p{font-size:7.5px;color:var(--navy);margin:8px 0 6px}
.form .row{display:flex;gap:6px}
.field{flex:1;height:18px;border:1px solid #ccc;background:var(--white);font-size:6.5px;color:#999;padding:4px 5px}
.area{height:50px;margin-top:6px;width:100%}
.submit{display:inline-block;background:var(--gold);color:var(--white);font-size:7.5px;font-weight:700;padding:4px 12px;margin-top:7px;border-radius:2px}
.courses,.quotes{margin-top:10px}
.course{display:flex;gap:10px;height:58px;margin-bottom:12px}
.course .thumb{width:80px;height:52px;background:linear-gradient(135deg,#3a4c7a,#9aa8c4)}
.course h4{font-size:7.5px;color:var(--navy);font-weight:700}
.course p{font-size:6px;color:var(--muted);margin-top:3px}
.btn-date{display:inline-block;background:var(--orange);color:var(--white);font-size:6px;font-weight:700;padding:3px 8px;margin-top:5px}
.quote{margin-bottom:16px}
.quote h4{font-size:7px;font-weight:700;color:var(--navy);line-height:1.35}
.quote p{font-size:6px;color:var(--muted);line-height:1.5;margin-top:3px}
.viewall{font-size:6.5px;color:var(--muted);margin-top:2px}
.footer{position:absolute;left:0;top:1040px;width:699px;height:138px;background:var(--navy);color:#c9d4ee}
.footer .inner{width:500px;margin:0 auto;display:flex;gap:30px;padding-top:20px;position:relative}
.fcol{width:88px}
.fcol h5{font-size:9px;color:var(--white);font-weight:600;margin-bottom:8px}
.fcol ul{list-style:none;font-size:6.5px;line-height:1.65}
.social li{display:flex;align-items:center;gap:5px;margin-bottom:5px}
.social i{width:11px;height:11px;background:#3c62b4;display:block}
.fbrand{position:absolute;right:0;top:10px;text-align:center;width:70px}
.fbrand .mark{width:56px;height:56px;border-radius:50%;background:var(--gold);border:4px solid var(--white);margin:0 auto}
.fbrand .name{font-size:8px;font-weight:800;color:var(--white);margin-top:4px;text-transform:uppercase}
.copy{position:absolute;left:0;top:1178px;width:699px;height:22px;background:var(--navy-dark);color:#aab6d4;font-size:6.5px;text-align:center;line-height:22px}
</style>
</head>
<body>
<header class="header">
  <div class="brand"><div class="mark"></div><div class="name">Brixlane Consulting</div></div>
  <div class="cta-courses">Upcoming Courses</div>
  <div class="phone">
    <svg width="14" height="14" viewBox="0 0 24 24"><path fill="#1f56b8" d="M6.6 10.8a15.1 15.1 0 0 0 6.6 6.6l2.2-2.2c.3-.3.7-.4 1-.2 1.1.4 2.3.6 3.6.6.6 0 1 .4 1 1V20c0 .6-.4 1-1 1A17 17 0 0 1 3 4c0-.6.4-1 1-1h3.5c.6 0 1 .4 1 1 0 1.3.2 2.5.6 3.6.1.3 0 .7-.2 1z"/></svg>
    978.555.0147
  </div>
</header>
<nav class="nav"><ul><li>Home</li><li>About Us</li><li>Free Resources</li><li>Police Promotions</li><li>Police Employment</li><li>Department Services</li></ul></nav>

<main class="wrap">
  <section class="hero" role="img" aria-label="Photo of uniformed police officers saluting in front of a national flag">
    <div class="tag">EXCELLENCE IN SERVICE</div>
    <h1>ARE YOU READY TO<br>ENHANCE YOUR CAREER?</h1>
    <div class="btns"><span class="btn-red">Register Now!</span><span class="btn-gold"></span></div>
    <span class="arrow" style="left:8px"></span><span class="arrow" style="right:8px"></span>
  </section>

  <section class="services">
    <div class="svc"><div class="pic" role="img" aria-label="Officer studying for a promotion exam"></div><h3>POLICE PROMOTIONAL PREPARATION</h3><p>Study guides, practice exams and review classes that help officers prepare for every promotional test.</p><span class="btn-navy">Learn More</span></div>
    <div class="svc"><div class="pic" role="img" aria-label="Candidate at a police entrance exam"></div><h3>POLICE EMPLOYMENT PREPARATION</h3><p>Entrance exam practice, oral board coaching and fitness guidance for future police officers.</p><span class="btn-navy">Learn More</span></div>
    <div class="svc"><div class="pic" role="img" aria-label="Officers in a training session"></div><h3>POLICE TRAINING &amp; EDUCATION</h3><p>Classroom courses in criminal law, report writing and procedure taught by experienced instructors.</p><span class="btn-navy">Learn More</span></div>
    <div class="svc"><div class="pic" role="img" aria-label="Police department command staff meeting"></div><h3>LAW ENFORCEMENT AGENCY SERVICES</h3><p>Assessment centers, exam development and consulting services designed for police departments.</p><span class="btn-navy">Learn More</span></div>
  </section>

  <div class="rule"></div>

  <section class="cols">
    <div class="col">
      <h2>Our <span>Products</span></h2>
      <ul class="products">
        <li><i></i>EASTPORT SERGEANT EXAM</li>
        <li><i></i>POLICE PROMOTIONS</li>
        <li><i></i>POLICE TRAINING &amp; REFERENCE</li>
        <li><i></i>COURSES</li>
        <li><i></i>MILLBROOK POLICE PRODUCTS</li>
      </ul>
    </div>
    <div class="col form">
      <h2>Send us <span>an Email</span></h2>
      <p>FOR FREE Promotions Exam Practice Questions</p>
      <div class="row"><div class="field">Your Name</div><div class="field">Your Email</div></div>
      <div class="field area">Type your Question Here</div>
      <span class="submit">Submit</span>
    </div>
  </section>

  <div class="rule lower"></div>

  <section class="cols">
    <div class="col">
      <h2>Upcoming <span>Courses</span></h2>
      <div class="courses">
        <div class="course"><div class="thumb" role="img" aria-label="Course banner for criminal law class"></div><div><h4>Criminal Law and Procedure for 6/7</h4><p>Two day review for officers</p><span class="btn-date">Learn More</span></div></div>
        <div class="course"><div class="thumb" role="img" aria-label="Officer writing a report"></div><div><h4>Effective Report Writing</h4><p>Clear reports that hold up</p><span class="btn-date">Learn More</span></div></div>
        <div class="course"><div class="thumb" role="img" aria-label="Classroom of officers"></div><div><h4>Post Sgt Law Class</h4><p>Law update for new sergeants</p><span class="btn-date">Learn More</span></div></div>
      </div>
      <div class="viewall">VIEW ALL ›</div>
    </div>
    <div class="col">
      <h2><span>Testimonials</span></h2>
      <div class="quotes">
        <div class="quote"><h4>Chief Daniel R. Colvin<br>Harwick Police Department</h4><p>"Our officers prepared with these materials and the results showed on exam day. The review classes were focused, practical and well organized, and every candidate felt ready for the written test and the oral board. We will use this team again."</p></div>
        <div class="quote"><h4>Major Lena Ortiz<br>Westbury Police Department</h4><p>"The training was professional from start to finish. Instructors knew the material, answered every question and kept the class engaged. Our department recommends these courses to any agency planning a promotional process."</p></div>
      </div>
      <div class="viewall">VIEW ALL ›</div>
    </div>
  </section>
</main>

<footer class="footer">
  <div class="inner">
    <div class="fcol"><h5>Site Links</h5><ul><li>Home</li><li>About Us</li><li>Free Resources</li><li>Police Promotions</li><li>Police Employment</li><li>Department Services</li></ul></div>
    <div class="fcol"><h5>Upcoming Courses</h5><ul><li>Criminal Law Review</li><li>Effective Report Writing</li><li>Post Sgt Law Class</li><li>Interview &amp; Oral Boards</li><li>Police Officer Entrance</li><li>Sergeant Study Group</li><li>The Law Review</li></ul></div>
    <div class="fcol social"><h5>Social Links</h5><ul><li><i></i>Circlebook</li><li><i></i>Chirper</li><li><i></i>ProLink</li></ul></div>
    <div class="fcol"><h5>Contact Us</h5><ul><li>Brixlane Consulting, LLC</li><li>PO Box 410</li><li>Northfield, MA 01360</li><li>978.555.0147</li><li>www.brixlaneprep.us</li></ul></div>
    <div class="fbrand"><div class="mark"></div><div class="name">Brixlane</div></div>
  </div>
</footer>
<div class="copy">Copyright © 2014 Brixlane Consulting. All Rights Reserved.</div>
</body>
</html>
```